BrightLatch Locksmith Box truck wrap sign/billboard

We recently purchased a box truck that we plan on parking in front of our office building.
as a sign/ "billboard".
Our shop is located in an office building on a very busy street, but cant seen from the road.
The idea is to pull customer attention and also kind of let them know our office is located right there.
The truck is going to park in reverse to the street.
I thought about a big logo with a dominant colors, that will pull attention to the direction I want , maybe an arrow or something similar to explain the direction of the shop.
I would love to have the company name and information on top of bunch of keys pics.
I attached a pic of my existed truck just as an example of keys pic.
also attached the logo, QR code.

company name: BrightLatch Locksmith
phone number: 404-582-9137
address: 4187 Hollowmere Rd NE #312 Atlanta, GA 30417
website www.brightlatchlocksmith-demo.com
services we can provide: Commercial , Residential, automotive, safes.

Details of the truck:
Varlo cargo van 2014 t4200
back of the truck dimensions :are 84.5x84.5
the side are: 145x78.5
the little are on the side are 18 1/4 x35.5

I attached a few pictures of the truck. Let me know what you think or if you have any other questions
Thank you so much.

Target Market(s)

customer attention that driving by

Industry/Entity Type

Locksmith

Requirements
Must have
• company name phone number services we provide pictures of car keys
Nice to have
• my logo is gray so i would like a colors that can flow with it but also pull lot of attention.

```html
<!DOCTYPE html>
<html lang="en">
<head>
<meta charset="utf-8">
<title>BrightLatch Locksmith – Box Truck Wrap</title>
<link href="https://fonts.googleapis.com/css2?family=Oswald:wght@500;600;700&display=swap" rel="stylesheet">
<style>
  :root {
    --page: #e4e5e3;
    --black: #050505;
    --yellow: #f2c80f;
    --panel: #f1f1ee;
    --silver: #c9c9c6;
    --ink: #111111;
    --photo-warm: #8a6a52;
    --photo-cool: #6f7c84;
    --safe-tones: linear-gradient(90deg, #c9cbc9, #7d8790 35%, #b9242b 55%, #2d3440 75%, #d9d6cc);
    --hardware-tones: linear-gradient(135deg, #dcdcdc, #9ea3a6 50%, #e7e7e4);
  }
  * { box-sizing: border-box; margin: 0; padding: 0; }
  html, body { width: 1076px; height: 1200px; overflow: hidden; }
  body {
    background: var(--page);
    font-family: "Oswald", sans-serif;
    position: relative;
  }
  .wrap-side {
    position: absolute;
    left: 18px;
    width: 1040px;
    height: 450px;
  }
  .wrap-side--driver { top: 70px; }
  .wrap-side--passenger { top: 640px; }

  .header-band {
    position: absolute;
    top: 0; left: 0;
    width: 1040px; height: 140px;
    background: var(--black);
  }
  .wrap-side--driver .header-band { border-radius: 34px 0 0 0; }
  .wrap-side--passenger .header-band { border-radius: 0 34px 0 0; }

  .brand-name {
    position: absolute;
    top: 14px;
    font-weight: 700;
    font-size: 76px;
    line-height: 1;
    color: var(--silver);
    letter-spacing: 0.5px;
    white-space: nowrap;
  }
  .wrap-side--driver .brand-name { left: 232px; width: 808px; text-align: center; }
  .wrap-side--passenger .brand-name { left: 0; width: 808px; text-align: center; }

  .box-body {
    position: absolute;
    top: 140px;
    width: 808px;
    height: 310px;
    background: var(--panel);
    display: flex;
    flex-direction: column;
  }
  .wrap-side--driver .box-body { left: 232px; }
  .wrap-side--passenger .box-body { left: 0; }

  .rule { height: 6px; background: var(--yellow); flex: none; }

  .services-area {
    height: 174px;
    display: flex;
    flex: none;
  }
  .services-list {
    flex: none;
    width: 400px;
    display: flex;
    flex-direction: column;
    justify-content: center;
    padding: 18px 22px 0;
    gap: 2px;
  }
  .services-list li {
    list-style: none;
    font-weight: 600;
    font-size: 35px;
    line-height: 1.3;
    color: var(--ink);
    white-space: nowrap;
  }
  .wrap-side--passenger .services-list { align-items: flex-end; }

  .product-gallery { flex: 1; display: flex; gap: 8px; padding: 8px; }
  .product-hardware { flex: 1; background: var(--hardware-tones); }
  .product-safes { flex: 1.4; background: var(--safe-tones); }

  .photo-strip {
    height: 86px;
    display: flex;
    gap: 6px;
    background: var(--yellow);
    flex: none;
  }
  .photo-strip .photo { flex: 1; }
  .photo--door { background: linear-gradient(90deg, #9aa3a8, var(--photo-warm)); }
  .photo--deadbolt { background: linear-gradient(90deg, #7e8a5e, #2a2a2a 60%, #c8b39a); }
  .photo--car { background: linear-gradient(90deg, #a8513d, #c9a88a 50%, #6f8090); }
  .photo--lever { background: linear-gradient(90deg, var(--photo-cool), #b9b4ad); }
  .photo--keypad { background: linear-gradient(90deg, #3a3f48, #8a8f95 60%, #d4d4d0); }

  .info-bar {
    height: 38px;
    background: var(--yellow);
    display: flex;
    align-items: center;
    justify-content: space-between;
    padding: 0 22px;
    flex: none;
  }
  .info-item {
    display: flex;
    align-items: center;
    gap: 10px;
    font-weight: 600;
    font-size: 18px;
    color: var(--ink);
    white-space: nowrap;
  }
  .info-item svg { width: 18px; height: 18px; flex: none; }

  .phone-pill {
    position: absolute;
    top: 112px;
    height: 54px;
    width: 340px;
    border-radius: 27px;
    background: var(--black);
    border: 4px solid var(--yellow);
    display: flex;
    align-items: center;
    justify-content: center;
    gap: 10px;
    color: var(--silver);
    font-weight: 700;
    font-size: 38px;
    z-index: 2;
  }
  .phone-pill svg { width: 36px; height: 36px; }
  .wrap-side--driver .phone-pill { left: 466px; }
  .wrap-side--passenger .phone-pill { left: 234px; }
</style>
</head>
<body>

<section class="wrap-side wrap-side--driver" aria-label="Driver side wrap">
  <div class="header-band"></div>
  <h1 class="brand-name">BrightLatch Locksmith</h1>
  <div class="phone-pill">
    <svg viewBox="0 0 36 36" aria-hidden="true"><circle cx="18" cy="18" r="16" fill="var(--silver)"/><path d="M12 9c1-1 2-1 3 0l2 3c.6 1 .4 2-.4 2.6l-1.2 1c1 2.2 2.6 3.8 4.8 4.8l1-1.2c.6-.8 1.6-1 2.6-.4l3 2c1 1 1 2 0 3l-1.4 1.4c-1.6 1.6-5 .8-8.6-2.8S9 13 10.6 10.4Z" fill="var(--black)"/></svg>
    <span>404-582-9137</span>
  </div>
  <div class="box-body">
    <div class="rule"></div>
    <div class="services-area">
      <ul class="services-list">
        <li>AUTOMOTIVE LOCKSMITH!</li>
        <li>RESIDENTIAL LOCKSMITH!</li>
        <li>COMMERCIAL LOCKSMITH!</li>
      </ul>
      <div class="product-gallery">
        <div class="product-hardware" role="img" aria-label="Door levers, keypad lock and mortise lock hardware"></div>
        <div class="product-safes" role="img" aria-label="Assorted security safes in grey, red, black and blue"></div>
      </div>
    </div>
    <div class="rule"></div>
    <div class="photo-strip">
      <div class="photo photo--door" role="img" aria-label="Technician fitting a lock on a wooden door"></div>
      <div class="photo photo--deadbolt" role="img" aria-label="Key turning in a deadbolt"></div>
      <div class="photo photo--car" role="img" aria-label="Driver holding up car keys through a vehicle window"></div>
      <div class="photo photo--lever" role="img" aria-label="Key inserted in a door lever lock"></div>
      <div class="photo photo--keypad" role="img" aria-label="Business person using an electronic keypad lock"></div>
    </div>
    <div class="info-bar">
      <span class="info-item">
        <svg viewBox="0 0 18 18" aria-hidden="true"><circle cx="9" cy="9" r="8" fill="var(--ink)"/><ellipse cx="9" cy="9" rx="3.4" ry="7" fill="none" stroke="var(--yellow)" stroke-width="1.3"/><path d="M1.5 9h15M3 5h12M3 13h12" stroke="var(--yellow)" stroke-width="1.3"/></svg>
        www.brightlatchlocksmith-demo.com
      </span>
      <span class="info-item">
        <svg viewBox="0 0 18 18" aria-hidden="true"><circle cx="9" cy="9" r="8" fill="var(--ink)"/><path d="M9 4a3.2 3.2 0 0 0-3.2 3.2C5.8 10 9 13.5 9 13.5s3.2-3.5 3.2-6.3A3.2 3.2 0 0 0 9 4Z" fill="var(--yellow)"/><circle cx="9" cy="7.2" r="1.2" fill="var(--ink)"/></svg>
        4187 Hollowmere Rd, NE #312 Atlanta, GA 30417
      </span>
    </div>
  </div>
</section>

<section class="wrap-side wrap-side--passenger" aria-label="Passenger side wrap">
  <div class="header-band"></div>
  <h2 class="brand-name">BrightLatch Locksmith</h2>
  <div class="phone-pill">
    <svg viewBox="0 0 36 36" aria-hidden="true"><circle cx="18" cy="18" r="16" fill="var(--silver)"/><path d="M12 9c1-1 2-1 3 0l2 3c.6 1 .4 2-.4 2.6l-1.2 1c1 2.2 2.6 3.8 4.8 4.8l1-1.2c.6-.8 1.6-1 2.6-.4l3 2c1 1 1 2 0 3l-1.4 1.4c-1.6 1.6-5 .8-8.6-2.8S9 13 10.6 10.4Z" fill="var(--black)"/></svg>
    <span>404-582-9137</span>
  </div>
  <div class="box-body">
    <div class="rule"></div>
    <div class="services-area">
      <div class="product-gallery">
        <div class="product-safes" role="img" aria-label="Assorted security safes in grey, red, black and blue"></div>
        <div class="product-hardware" role="img" aria-label="Door levers, keypad lock and mortise lock hardware"></div>
      </div>
      <ul class="services-list">
        <li>AUTOMOTIVE LOCKSMITH!</li>
        <li>RESIDENTIAL LOCKSMITH!</li>
        <li>COMMERCIAL LOCKSMITH!</li>
      </ul>
    </div>
    <div class="rule"></div>
    <div class="photo-strip">
      <div class="photo photo--door" role="img" aria-label="Technician fitting a lock on a wooden door"></div>
      <div class="photo photo--deadbolt" role="img" aria-label="Key turning in a deadbolt"></div>
      <div class="photo photo--car" role="img" aria-label="Driver holding up car keys through a vehicle window"></div>
      <div class="photo photo--lever" role="img" aria-label="Key inserted in a door lever lock"></div>
      <div class="photo photo--keypad" role="img" aria-label="Business person using an electronic keypad lock"></div>
    </div>
    <div class="info-bar">
      <span class="info-item">
        <svg viewBox="0 0 18 18" aria-hidden="true"><circle cx="9" cy="9" r="8" fill="var(--ink)"/><path d="M9 4a3.2 3.2 0 0 0-3.2 3.2C5.8 10 9 13.5 9 13.5s3.2-3.5 3.2-6.3A3.2 3.2 0 0 0 9 4Z" fill="var(--yellow)"/><circle cx="9" cy="7.2" r="1.2" fill="var(--ink)"/></svg>
        4187 Hollowmere Rd, NE #312 Atlanta, GA 30417
      </span>
      <span class="info-item">
        <svg viewBox="0 0 18 18" aria-hidden="true"><circle cx="9" cy="9" r="8" fill="var(--ink)"/><ellipse cx="9" cy="9" rx="3.4" ry="7" fill="none" stroke="var(--yellow)" stroke-width="1.3"/><path d="M1.5 9h15M3 5h12M3 13h12" stroke="var(--yellow)" stroke-width="1.3"/></svg>
        www.brightlatchlocksmith-demo.com
      </span>
    </div>
  </div>
</section>

</body>
</html>
```